Verdant Harbor wants proposals to design and develop a new website, tying together the visuals and branding message initiated with the package design. The goals of this website will be to provide an excellent user experience, to make the website a vital source of information that
will be indexed by the search engines and to facilitate and encourage consumer confidence.
The design and function of the website will be instrumental in generating knowledge of and trust in the product line.

Our current website Verdantharbor.com is an informational and transactional website. We are looking to completely overhaul the informational side. The products we sell are unique combinations of Ayurvedic herbal supplements. They are very effective and of a superior quality. However, the current website in all fairness is "blah". The site should be professional, visually enticing, reliable and efficient, compatible with virtually any computer that connects to it and makes for a first rate impression to our customers.

We want a website which will relay to the customer the effectiveness and superior quality of our products. We want the site to engage the customer. The website needs to be an experience and to connect to the customer emotionally. It is a tall order but it is what we need to deliver our message. A majority of the traffic comes from people already interested in a particular condition that our product is used for. Our goal is for the customer to be convinced that the solution is our product which it is in most cases.

The design should be able to handle fields that are currently on the site, like article links to external sites, video clips on products, specials, etc. The site is currently powered on the back end by .NET 4.0 with MVC architecture and this we hope to continue. Also, the text to HTML has to be a very good ratio.

The current pages are very well indexed and search engine optimized and that concept has to be preserved. At this point, we do not want to build a separate mobile version so flash is not an option.
Updates

Pleas come up with original ideas and not just refreshing currently what I have.

Pictures used need to be realistic.  Faces are ok to use but not necessary.  The picture/graphic needs to communicate effectiveness and high quality of products.  Also the overall look and feel needs to be addressed.  Please don't take existing part of current website and paste onto new one.  

We are disappointed in the overall designs received.  They all look like cut and paste websites. One that we did like was showing herbs held in the hand.  We are not opposed to faces being shown but it has to look "real".  Also the space below the picture needs to be developed more.  We are not focusing on transactions on this website although a link will be provided for those interested in purchasing.

After reviewing all designs, it seems showing herbs/flowers/nature is a better way to go.  The picture of women makes our company look more like a spa which is not our intent.  

Target Market(s)

USA, Canada, Western European customers; 60% Females, 40% male; 35 plus age group

Industry/Entity Type

Architecture

Requirements
Must have
• Good Text to Html ratio. Should be SEO compatible. Feel good and engaging audience.
Should not have
• Must be mobile compatible and should not be flash based.

```html
<!DOCTYPE html>
<html lang="en">
<head>
<meta charset="utf-8">
<title>Verdant Harbor — Herbal Supplements &amp; Skincare</title>
<link href="https://fonts.googleapis.com/css2?family=Open+Sans:wght@300;400;600&family=Philosopher:wght@700&family=Arimo:wght@400;700&display=swap" rel="stylesheet">
<style>
:root{
  --leaf:#6ea61c;
  --leaf-dark:#4f7d12;
  --leaf-light:#a9d45a;
  --olive:#6b6b12;
  --olive-deep:#5a5a0c;
  --ink:#2b2b2b;
  --muted:#8a8a8a;
  --paper:#ffffff;
  --mist:#ececec;
  --mist-dark:#d9d9d9;
  --price:#7cb41f;
}
*{box-sizing:border-box;margin:0;padding:0}
html,body{width:1200px;height:2193px;overflow:hidden;background:var(--paper)}
body{position:relative;font-family:"Arimo",Arial,sans-serif;color:var(--ink)}
.abs{position:absolute}

/* top band */
.top-band{left:0;top:0;width:1200px;height:95px;background:radial-gradient(ellipse at 30% 40%,#d9ecb0 0,#9fcb4e 45%,#6aa31d 100%)}
.utility-bar{left:832px;top:0;width:270px;height:31px;background:rgba(120,120,100,.55);border-radius:0 0 6px 6px;color:#fff;font-size:12px;line-height:31px;text-align:center}
.cart-icon{left:796px;top:4px}
.social-dots{left:983px;top:47px;display:flex;gap:8px}
.social-dots span{width:26px;height:26px;border-radius:50%;background:#2d2d2d;display:block}

/* nav */
.nav-bar{left:0;top:95px;width:1200px;height:95px;background:linear-gradient(#fff,#f1f1f1);box-shadow:0 2px 4px rgba(0,0,0,.15)}
.nav-item{top:124px;font-family:"Open Sans",sans-serif;font-size:16px;color:#222}
.nav-pill{left:78px;top:118px;width:130px;height:46px;background:linear-gradient(#8cc43a,var(--leaf-dark));border-radius:60px 8px 60px 8px;color:#fff;font-family:"Open Sans",sans-serif;font-size:16px;text-align:center;line-height:46px}
.logo-tab{left:397px;top:52px;width:363px;height:155px}
.brand-name{left:397px;top:108px;width:363px;text-align:center;font-family:"Open Sans",sans-serif;font-weight:600;font-size:34px;color:var(--olive-deep);letter-spacing:.5px}
.green-band{left:0;top:190px;width:1200px;height:60px;background:linear-gradient(90deg,#7fb42a,#b6dc72 50%,#7fb42a)}

/* hero */
.hero{left:0;top:240px;width:1200px;height:445px;background:#fff;border-radius:50% 50% 0 0/28px 28px 0 0}
.hero-kicker{left:117px;top:300px;font-family:"Open Sans",sans-serif;font-weight:400;font-size:26px;color:var(--olive)}
.hero-title{left:115px;top:330px;font-family:"Open Sans",sans-serif;font-weight:300;font-size:58px;line-height:60px;color:var(--olive)}
.hero-title .amp{color:var(--leaf-dark)}
.hero-sub{left:115px;top:455px;font-family:"Open Sans",sans-serif;font-weight:300;font-size:42px;color:var(--leaf-dark)}
.search{left:117px;top:580px;width:224px;height:35px;border:1px solid #bdbdbd;background:#fff;font-size:12px;color:#444;line-height:33px;padding-left:12px}
.search-btn{position:absolute;right:3px;top:3px;width:27px;height:27px;background:#ececec;border:1px solid #ccc;text-align:center;line-height:25px;color:#666}
.hero-image{left:510px;top:245px;width:630px;height:445px;border-radius:46% 42% 30% 40%;background:radial-gradient(ellipse at 50% 40%,#8a8f6a 0,#b86b3c 35%,#e2a54a 55%,rgba(255,255,255,0) 75%)}

/* featured */
.featured{left:0;top:682px;width:1200px;height:328px;background:linear-gradient(#e3e3e3,#f4f4f4 40%,#e6e6e6)}
.featured-title{left:124px;top:700px;font-family:"Open Sans",sans-serif;font-size:22px;color:#444}
.product-card{top:746px;width:221px;height:216px;background:#fff;border:1px solid #cfcfcf;box-shadow:0 1px 3px rgba(0,0,0,.15)}
.product-card h3{height:42px;background:linear-gradient(#8cc43a,var(--leaf));color:#1e2a06;font-family:"Open Sans",sans-serif;font-weight:400;font-size:14px;text-align:center;line-height:42px}
.product-shot{position:absolute;left:55px;top:62px;width:110px;height:100px;background:linear-gradient(135deg,#efe6b8,#c7b56e);border-radius:3px}
.product-link{position:absolute;left:12px;bottom:14px;font-size:12px;color:#111;text-decoration:underline}
.price-tag{position:absolute;right:0;bottom:6px;width:100px;height:34px;background:var(--price);color:#fff;font-family:"Open Sans",sans-serif;font-weight:600;font-size:19px;line-height:34px;text-align:center;clip-path:polygon(14% 0,100% 0,100% 100%,14% 100%,0 50%)}
.slider-arrow{top:836px;width:38px;height:38px;background:#c9c9c9;color:#fff;text-align:center;line-height:38px;font-size:22px}

/* intro */
.intro-title{left:0;top:1040px;width:1200px;text-align:center;font-family:"Philosopher",serif;font-size:29px;color:var(--olive);letter-spacing:1px}
.intro-text{left:0;top:1090px;width:1200px;text-align:center;font-size:12px;line-height:17px;color:var(--muted)}
.offer-title{left:0;top:1136px;width:1200px;text-align:center;font-family:"Open Sans",sans-serif;font-weight:300;font-size:28px;color:#444}
.offer-sub{left:0;width:1200px;text-align:center;font-size:15px;color:#222}
.offer-note{left:0;width:1200px;text-align:center;font-size:12px;color:var(--muted)}

/* services band */
.services{left:0;top:1278px;width:1200px;height:400px}
.service{top:1378px;width:300px;text-align:center;font-family:"Open Sans",sans-serif}
.service h4{font-weight:400;font-size:24px;color:#333}
.service p{font-size:14px;color:#3a4a1a;margin-top:4px}
.service-disc{top:1447px;width:180px;height:180px;border-radius:50%;background:radial-gradient(#f4f4f4,#d6d6d6);border:4px solid #eaeaea;box-shadow:0 3px 8px rgba(0,0,0,.3);display:flex;align-items:center;justify-content:center}

/* standards */
.aloe{left:0;top:1720px;width:520px;height:400px;border-radius:40% 60% 0 0;background:radial-gradient(ellipse at 30% 70%,#8fbf5c 0,#b9d98f 40%,rgba(255,255,255,0) 72%)}
.standards-title{left:447px;top:1712px;font-family:"Open Sans",sans-serif;font-size:26px;color:#111}
.standards-list{left:447px;top:1767px;width:650px;list-style:none;font-family:"Open Sans",sans-serif;font-size:18px;line-height:31px;color:#333}
.standards-list li::before{content:"• "}

/* footer */
.footer{left:0;top:2115px;width:1200px;height:78px;background:linear-gradient(#4f8a12,#2f5c05)}
.footer-copy{left:93px;top:2133px;font-size:11px;color:#eaf3da;line-height:18px}
.footer-logo{left:855px;top:2063px;width:259px;height:120px}
.footer-brand{left:855px;top:2105px;width:259px;text-align:center;font-family:"Open Sans",sans-serif;font-weight:600;font-size:26px;color:var(--olive-deep)}
</style>
</head>
<body>

<header>
  <div class="abs top-band"></div>
  <svg class="abs cart-icon" width="30" height="24" viewBox="0 0 30 24" aria-hidden="true"><path d="M2 3h5l4 12h13l3-9H9" fill="none" stroke="#222" stroke-width="2.2"/><circle cx="12" cy="20" r="2" fill="#222"/><circle cx="22" cy="20" r="2" fill="#222"/></svg>
  <nav class="abs utility-bar">Home | Bookmark | Sitemap | Contact Us</nav>
  <div class="abs social-dots" aria-label="Social links"><span></span><span></span><span></span></div>

  <div class="abs nav-bar"></div>
  <div class="abs nav-pill">Suppliments</div>
  <div class="abs nav-item" style="left:213px">Skin Care</div>
  <div class="abs nav-item" style="left:308px">Our Retailer</div>
  <div class="abs nav-item" style="left:760px">Articals/Studies</div>
  <div class="abs nav-item" style="left:896px">About Us</div>
  <div class="abs nav-item" style="left:986px">Register/ Inquires</div>

  <svg class="abs logo-tab" viewBox="0 0 363 155" aria-hidden="true">
    <polygon points="0,45 40,45 30,75" fill="#6ea61c"/>
    <polygon points="323,45 363,45 333,75" fill="#6ea61c"/>
    <polygon points="28,0 335,0 325,150 38,150" fill="#f2f2f2" stroke="#dcdcdc"/>
  </svg>
  <div class="abs brand-name">Verdant Harbor</div>
  <div class="abs green-band"></div>
</header>

<section>
  <div class="abs hero"></div>
  <div class="abs hero-image" role="img" aria-label="Photo of a stone mortar and pestle with fresh herbs, dried chillies, turmeric roots, star anise, cardamom and orange lilies"></div>
  <p class="abs hero-kicker">YOUR JOURNEY TO NATION LOVING</p>
  <h1 class="abs hero-title">All Verdant Harbor<br>Suppliments <span class="amp">&amp;</span></h1>
  <p class="abs hero-sub">Skincare Products</p>
  <div class="abs search">Search By Keyword<span class="search-btn">&rsaquo;</span></div>
</section>

<section>
  <div class="abs featured"></div>
  <h2 class="abs featured-title">Feautured Product</h2>
  <div class="abs slider-arrow" style="left:81px">&lsaquo;</div>
  <div class="abs slider-arrow" style="left:1065px">&rsaquo;</div>

  <article class="abs product-card" style="left:123px"><h3>TURMERIC CURCUMIN</h3><div class="product-shot" role="img" aria-label="Turmeric curcumin product box with capsules"></div><a class="product-link">Product Detail&gt;&gt;</a><span class="price-tag">$ 24.99</span></article>
  <article class="abs product-card" style="left:363px"><h3>BLOOD SUGAR SUPPLEMENTS</h3><div class="product-shot" role="img" aria-label="Blood sugar supplement product box with capsules"></div><a class="product-link">Product Detail&gt;&gt;</a><span class="price-tag">$ 24.99</span></article>
  <article class="abs product-card" style="left:601px"><h3>NATURAL SLEEP AID</h3><div class="product-shot" role="img" aria-label="Natural sleep aid product box with capsules"></div><a class="product-link">Product Detail&gt;&gt;</a><span class="price-tag">$ 24.99</span></article>
  <article class="abs product-card" style="left:841px"><h3>LIBIDO SUPPLEMENTS</h3><div class="product-shot" role="img" aria-label="Libido supplement product box with capsules"></div><a class="product-link">Product Detail&gt;&gt;</a><span class="price-tag">$ 24.99</span></article>
</section>

<section>
  <h2 class="abs intro-title">HERBAL NATURAL SUPPLEMENTS: AUTHENTIC FORMULAS</h2>
  <p class="abs intro-text">All of our Herbal Natural Supplements and Skincare Products are made using authentic ancient time tested formulations<br>and have an excellent track record.</p>
  <h2 class="abs offer-title">WHAT WE OFFER IS UNIQUE</h2>
  <p class="abs offer-sub" style="top:1182px">Multi-herb Supplements Like</p>
  <p class="abs offer-note" style="top:1206px">Turmeric Curcumin; Blood sugar supplements; Stress supplements; Libido supplements, Natural sleep aid and others.*</p>
  <p class="abs offer-sub" style="top:1234px">Natural skin care formulas like</p>
  <p class="abs offer-note" style="top:1258px">Saffron &amp; Cucumber Under eye cream; Apricot &amp; Almond Anti wrinkle cream and others.</p>
</section>

<section>
  <svg class="abs services" viewBox="0 0 1200 400" preserveAspectRatio="none" role="img" aria-label="Soft blurred green foliage background">
    <defs>
      <radialGradient id="foliage" cx="50%" cy="50%" r="70%"><stop offset="0" stop-color="#d8ecaa"/><stop offset=".5" stop-color="#9bc94a"/><stop offset="1" stop-color="#5f9a18"/></radialGradient>
    </defs>
    <path d="M0,0 Q600,60 1200,0 V400 Q600,330 0,400 Z" fill="url(#foliage)"/>
    <path d="M380,40 Q600,22 820,40 Q600,30 380,40Z" fill="#6f7f3a" opacity=".6"/>
  </svg>
  <div class="abs service" style="left:126px"><h4>FREE SHIPPING</h4><p>on orders of $20 or more</p></div>
  <div class="abs service" style="left:440px"><h4>TESTIMONIALS</h4><p>&amp; Reviews</p></div>
  <div class="abs service" style="left:755px"><h4>SOCIAL</h4><p>Chatter, Facepage, Viewtube...</p></div>

  <div class="abs service-disc" style="left:186px">
    <svg width="76" height="76" viewBox="0 0 76 76" aria-hidden="true"><rect x="6" y="10" width="64" height="58" fill="none" stroke="#222" stroke-width="5"/><path d="M6 10 L20 2 H56 L70 10" fill="none" stroke="#222" stroke-width="4"/><path d="M38 24 L24 40 H33 V58 H43 V40 H52 Z" fill="#222"/></svg>
  </div>
  <div class="abs service-disc" style="left:500px">
    <svg width="90" height="70" viewBox="0 0 90 70" aria-hidden="true"><ellipse cx="34" cy="28" rx="30" ry="22" fill="#222"/><path d="M14 44 L8 62 L30 48Z" fill="#222"/><ellipse cx="60" cy="38" rx="26" ry="19" fill="#222" stroke="#e4e4e4" stroke-width="4"/><path d="M74 52 L84 66 L62 56Z" fill="#222"/></svg>
  </div>
  <div class="abs service-disc" style="left:815px">
    <svg width="90" height="90" viewBox="0 0 90 90" aria-hidden="true"><g fill="#8a8a8a"><circle cx="16" cy="16" r="13"/><rect x="33" y="3" width="24" height="24" rx="3"/><rect x="62" y="3" width="24" height="24" rx="3"/><rect x="4" y="33" width="24" height="24" rx="3"/><rect x="33" y="33" width="24" height="24" rx="3"/><rect x="62" y="33" width="24" height="24" rx="3"/></g></svg>
  </div>
</section>

<section>
  <div class="abs aloe" role="img" aria-label="Photo of a fresh aloe vera plant"></div>
  <h2 class="abs standards-title">OUR HERBAL SUPPLEMENTS AND GOLD STANDARDS</h2>
  <ul class="abs standards-list">
    <li>All of our products are based on ancient time tested herbal formulas.</li>
    <li>All the products are designed to be condition specific.</li>
    <li>Non-GMO - All our supplements are made from ingredients that were not genetically engineered.</li>
    <li>We have conducted trials and studies on our products.</li>
    <li>We have attractive, eco friendly, hygienically packaged products.</li>
    <li>All of our products have standardized herbal formulas.</li>
  </ul>
</section>

<footer>
  <div class="abs footer"></div>
  <p class="abs footer-copy">© 2013 Verdantharbor.com. All Rights Reserved<br>Home |Help/Customer Support |Shipping Rates &amp; Information |Returns |Terms of Use |FAQ |Privacy Policy |</p>
  <svg class="abs footer-logo" viewBox="0 0 259 120" aria-hidden="true">
    <polygon points="0,40 30,40 22,62" fill="#6ea61c"/>
    <polygon points="229,40 259,40 237,62" fill="#6ea61c"/>
    <polygon points="20,0 239,0 232,120 27,120" fill="#f2f2f2" stroke="#dcdcdc"/>
  </svg>
  <div class="abs footer-brand">Verdant Harbor</div>
</footer>

</body>
</html>
```